Flyer-Design für Energieberatungsunternehmen
Zielgruppe
Wir sind ein Energieberatungsunternehmen und wollen schwerpunktmäßig Stadtwerke und andere Energieversorgungsunternehmen im Bereich der Fernwärmeversorgung beraten.
Aufgabenstellung
DIN A4 quer, faltbar (3 Spalten je auf Vorder- und Rückseite)
Einfaches Flyermuster mit Strukturvorgaben und Inhalten wird beigefügt.

```html
<!DOCTYPE html>
<html lang="de">
<head>
<meta charset="utf-8">
<title>Mesura.Energy – Flyer Titelseite</title>
<link rel="stylesheet" href="https://fonts.googleapis.com/css2?family=Montserrat:wght@300;400;600;800&display=swap">
<style>
  :root {
    --stage: #e9ebef;
    --navy: #1b2f66;
    --blue: #1d5796;
    --blue-light: #3a74ad;
    --band: #0a1430;
    --text: #ffffff;
    --text-soft: #e4ebf5;
  }
  * { margin: 0; padding: 0; box-sizing: border-box; }
  html, body {
    width: 1200px; height: 675px; overflow: hidden;
    background: var(--stage);
    font-family: "Montserrat", Arial, sans-serif;
  }
  .canvas {
    width: 1200px; height: 675px;
    display: flex; align-items: center; justify-content: center;
  }
  .flyer-cover {
    position: relative;
    width: 304px; height: 640px;
    overflow: hidden;
    background: linear-gradient(160deg, var(--blue) 40%, var(--blue-light) 100%);
    box-shadow: 0 6px 24px rgba(10, 20, 50, 0.25);
  }
  .cover-visual {
    position: absolute; left: 0; top: 0;
    width: 100%; height: 350px;
    background:
      radial-gradient(circle at 55% 50%, #eaf3ff 0%, #8fb4e0 8%, #33558f 22%, transparent 45%),
      linear-gradient(150deg, var(--navy) 0%, #28407a 50%, #3c3f77 100%);
  }
  .cover-band {
    position: absolute; left: 0; top: 300px;
    width: 100%; height: 120px;
  }
  .cover-text {
    position: absolute; left: 20px; right: 16px; top: 382px;
    color: var(--text);
    white-space: nowrap;
  }
  .headline {
    font-weight: 300;
    font-size: 30px;
    line-height: 1.1;
  }
  .subline {
    font-weight: 300;
    font-size: 15.5px;
    color: var(--text-soft);
    margin-top: 4px;
  }
  .claim {
    font-weight: 800;
    font-size: 28px;
    line-height: 1.1;
    margin-top: 12px;
    color: #f2f4f8;
  }
  .brand {
    position: absolute; left: 0; right: 0; top: 540px;
    text-align: center; color: var(--text);
    white-space: nowrap;
  }
  .brand-name {
    display: inline-flex; align-items: center; gap: 8px;
    font-weight: 600; font-size: 23px; letter-spacing: -0.3px;
  }
  .brand-dot {
    width: 13px; height: 13px; background: var(--text);
  }
  .brand-url {
    font-weight: 400; font-size: 12px; letter-spacing: 3px;
    margin-top: 8px; color: var(--text-soft);
  }
</style>
</head>
<body>
<main class="canvas">
  <article class="flyer-cover">
    <div class="cover-visual" role="img" aria-label="Foto: Hand hält eine Lupe mit leuchtender Glühbirne, umgeben von Symbolen erneuerbarer Energien"></div>
    <svg class="cover-band" viewBox="0 0 304 120" preserveAspectRatio="none" aria-hidden="true">
      <polygon points="0,30 304,70 304,120 0,120" fill="#1d5796"/>
      <polygon points="0,0 304,50 304,70 0,30" fill="#0a1430"/>
      <polygon points="150,48 304,70 304,82" fill="#16305e" opacity="0.7"/>
    </svg>
    <section class="cover-text">
      <h1 class="headline">Energieberatung</h1>
      <p class="subline">nach dem Mesura-Prinzip:</p>
      <p class="claim">Genau richtig!</p>
    </section>
    <footer class="brand">
      <div class="brand-name"><span class="brand-dot"></span>Mesura.Energy</div>
      <div class="brand-url">www.mesura.energy</div>
    </footer>
  </article>
</main>
</body>
</html>
```